Need a sleek, professional business card design for a Web Development business

I need a unique business card designed for a web development company. It is also the parent company for any ventures I do, such as my ClipHarbor channel, startup ideas I have, etc. I am the single member of "Copper Lantern Sites LLC." I will attach my basic logo here, so you will see the current color scheme and have the asset available. Thank you!

Target Market(s)

Startups, SMB's, Professionals

Industry/Entity Type

Business

Font styles to use
Other font styles liked:
• Lovello for headings is what I use, but not necessary.

Colors

Designer to choose colors to be used in the design.

Requirements
Nice to have
• Sleek is the word. Professional, modern, dark.
Should not have
• Any work from someone else's design. Lacking originality.

```html
<!DOCTYPE html>
<html lang="en">
<head>
<meta charset="utf-8">
<title>Copper Lantern Sites LLC – Business Card</title>
<link rel="stylesheet" href="https://fonts.googleapis.com/css2?family=Michroma&family=Josefin+Sans:wght@600;700&display=swap">
<style>
  :root {
    --page: #ffffff;
    --frame: #d6d6d6;
    --panel: #fdfdfd;
    --card-black: #1c1b19;
    --band-dark: #424242;
    --band-light: #737373;
    --text-light: #ffffff;
    --social: #b3b3b3;
    --accent: #f2a05a;
  }
  * { margin: 0; padding: 0; box-sizing: border-box; }
  html, body { width: 961px; height: 1200px; overflow: hidden; background: var(--page); }
  .sheet {
    position: relative; width: 961px; height: 1200px;
    border: 1px solid var(--frame); background: var(--page);
  }
  .mount {
    position: absolute; left: 60px; width: 839px; height: 480px;
    background: var(--panel); border: 1px solid #e4e4e4;
  }
  .mount--front { top: 90px; }
  .mount--mono { top: 629px; }
  .card {
    position: absolute; left: 28px; top: 28px; width: 782px; height: 424px; overflow: hidden;
  }
  .card__inner {
    position: absolute; left: 0; top: 0; width: 978px; height: 530px;
    transform: scale(0.8); transform-origin: 0 0;
  }
  .card__bg { position: absolute; inset: 0; width: 978px; height: 530px; }
  .brand {
    position: absolute; left: 60px; width: 346px; top: 358px; text-align: center;
    font-family: "Michroma", sans-serif; font-size: 19px; color: var(--accent);
    letter-spacing: 0.5px;
  }
  .card--mono .brand { color: var(--text-light); }
  .brand__suffix {
    display: flex; align-items: center; justify-content: center; gap: 12px;
    margin-top: 10px; font-size: 15px; letter-spacing: 5px;
  }
  .brand__suffix::before, .brand__suffix::after {
    content: ""; width: 96px; height: 1px; background: currentColor;
  }
  .identity {
    position: absolute; right: 75px; top: 82px; text-align: right; color: var(--text-light);
  }
  .identity__name {
    font-family: "Michroma", sans-serif; font-size: 33px; letter-spacing: 7px; line-height: 1;
  }
  .identity__role {
    margin-top: 14px; font-family: "Josefin Sans", sans-serif; font-weight: 700;
    font-size: 24px; letter-spacing: 6.5px; line-height: 1;
  }
  .contact { position: absolute; left: 543px; top: 268px; color: var(--text-light); }
  .contact__row { display: flex; align-items: center; gap: 20px; font-family: "Michroma", sans-serif; }
  .contact__row svg { width: 28px; height: 28px; flex: none; }
  .contact__row--phone { font-size: 25px; letter-spacing: 5px; height: 36px; }
  .contact__row--mail, .contact__row--web { font-size: 14px; letter-spacing: 2.6px; height: 28px; margin-top: 15px; }
  .contact__row--mail { margin-top: 22px; }
  .social {
    position: absolute; left: 543px; right: 70px; top: 482px; display: flex; justify-content: space-between;
    font-family: "Josefin Sans", sans-serif; font-weight: 700; font-size: 17px; color: var(--social);
  }
</style>
</head>
<body>
<main class="sheet">

  <section class="mount mount--front">
    <div class="card card--color">
      <div class="card__inner">
        <svg class="card__bg" viewBox="0 0 978 530" aria-hidden="true">
          <rect width="978" height="530" fill="var(--card-black)"/>
          <rect width="978" height="87" fill="var(--band-dark)"/>
          <polygon points="332,0 978,0 978,173 502,173" fill="var(--band-light)"/>
          <rect y="465" width="978" height="65" fill="var(--band-dark)"/>
          <polygon points="502,465 978,465 978,530 441,530" fill="var(--band-light)"/>
        </svg>
        <div class="brand">COPPER LANTERN SITES<div class="brand__suffix">LLC</div></div>
        <div class="identity">
          <div class="identity__name">ALEX MARLOW</div>
          <div class="identity__role">GENERAL DIRECTOR</div>
        </div>
        <div class="contact">
          <div class="contact__row contact__row--phone">
            <svg viewBox="0 0 28 28"><path d="M3 10c0-4 5-6 11-6s11 2 11 6v2h-6v-3H9v3H3z M8 13h12l3 10H5z" fill="#fff"/><circle cx="14" cy="18" r="3" fill="var(--card-black)"/></svg>
            <span>555.014.2290</span>
          </div>
          <div class="contact__row contact__row--mail">
            <svg viewBox="0 0 28 28"><rect x="1" y="6" width="26" height="16" fill="#fff"/><path d="M1 6l13 10 13-10" fill="none" stroke="var(--card-black)" stroke-width="1.6"/></svg>
            <span>alex.marlow@cls.com</span>
          </div>
          <div class="contact__row contact__row--web">
            <svg viewBox="0 0 28 28"><circle cx="14" cy="14" r="12" fill="#fff"/><path d="M2 14h24M14 2v24M5 7h18M5 21h18" stroke="var(--card-black)" stroke-width="1.4" fill="none"/><ellipse cx="14" cy="14" rx="6" ry="12" fill="none" stroke="var(--card-black)" stroke-width="1.4"/></svg>
            <span>www.copperlantern.com</span>
          </div>
        </div>
        <div class="social"><span>ClipHarbor</span><span>TalkWave</span><span>Friendly</span><span>ProNet</span><span>Blogly</span></div>
      </div>
    </div>
  </section>

  <section class="mount mount--mono">
    <div class="card card--mono">
      <div class="card__inner">
        <svg class="card__bg" viewBox="0 0 978 530" aria-hidden="true">
          <rect width="978" height="530" fill="var(--card-black)"/>
          <rect width="978" height="87" fill="var(--band-dark)"/>
          <polygon points="332,0 978,0 978,173 502,173" fill="var(--band-light)"/>
          <rect y="465" width="978" height="65" fill="var(--band-dark)"/>
          <polygon points="502,465 978,465 978,530 441,530" fill="var(--band-light)"/>
        </svg>
        <div class="brand">COPPER LANTERN SITES<div class="brand__suffix">LLC</div></div>
        <div class="identity">
          <div class="identity__name">ALEX MARLOW</div>
          <div class="identity__role">GENERAL DIRECTOR</div>
        </div>
        <div class="contact">
          <div class="contact__row contact__row--phone">
            <svg viewBox="0 0 28 28"><path d="M3 10c0-4 5-6 11-6s11 2 11 6v2h-6v-3H9v3H3z M8 13h12l3 10H5z" fill="#fff"/><circle cx="14" cy="18" r="3" fill="var(--card-black)"/></svg>
            <span>555.014.2290</span>
          </div>
          <div class="contact__row contact__row--mail">
            <svg viewBox="0 0 28 28"><rect x="1" y="6" width="26" height="16" fill="#fff"/><path d="M1 6l13 10 13-10" fill="none" stroke="var(--card-black)" stroke-width="1.6"/></svg>
            <span>alex.marlow@cls.com</span>
          </div>
          <div class="contact__row contact__row--web">
            <svg viewBox="0 0 28 28"><circle cx="14" cy="14" r="12" fill="#fff"/><path d="M2 14h24M14 2v24M5 7h18M5 21h18" stroke="var(--card-black)" stroke-width="1.4" fill="none"/><ellipse cx="14" cy="14" rx="6" ry="12" fill="none" stroke="var(--card-black)" stroke-width="1.4"/></svg>
            <span>www.copperlantern.com</span>
          </div>
        </div>
        <div class="social"><span>ClipHarbor</span><span>TalkWave</span><span>Friendly</span><span>ProNet</span><span>Blogly</span></div>
      </div>
    </div>
  </section>

</main>
</body>
</html>
```